Flask Their Crest needs wedding label designs!

Flask Their Crest is looking for new wedding designs! Please look at http://www.flasktheircrest.example/water-bottle-labels and http://www.flasktheircrest.example/custom-water to get an idea of what we currently offer.

These new designs will be saved onto Flask Their Crest so that customers can come and customize the text and/or add pictures on them for purchase as water bottle labels or custom label bottled water.

Designs must appeal to a broad audience so any and all styles will be considered. Some other sites to draw inspiration from are smallinkwell.example, greetvane.example, vowcardqueens.example and pressfold.example.

Questions? Ask away!

Target Market(s)

Target market is brides, mothers of brides and wedding planners.

Industry/Entity Type

Wedding

Requirements
Must have
• Designs must be at 300 dpi in CMYK. Width is 8.133" Height is 2.377" with a .125" bleed around all sides.

```html
<!DOCTYPE html>
<html lang="en">
<head>
<meta charset="UTF-8">
<title>Wedding Water Bottle Labels – WBL05 &amp; WBL06</title>
<link rel="stylesheet" href="https://fonts.googleapis.com/css2?family=Arimo:wght@700&family=Cinzel:wght@700&family=Roboto+Condensed:wght@300&display=swap">
<style>
  :root {
    --backdrop-centre: #ffffff;
    --backdrop-edge: #d6d6d6;
    --caption-grey: #8a8a8a;
    --berry: #a3236a;
    --berry-light: #c8579a;
    --cocoa: #653716;
    --peach: #fbc6b0;
    --peach-pattern: #f6b8a2;
    --lagoon: #0f83a7;
    --lagoon-pattern: #3c9cbd;
    --lagoon-edge: #0a6e8f;
    --deep-teal: #03445a;
    --white: #ffffff;
  }
  * { margin: 0; padding: 0; box-sizing: border-box; }
  html, body { width: 1200px; height: 900px; overflow: hidden; }
  body {
    position: relative;
    background: radial-gradient(ellipse at center, var(--backdrop-centre) 55%, var(--backdrop-edge) 100%);
  }
  .design-code {
    position: absolute;
    left: 131px;
    font: 300 20px/1 "Roboto Condensed", sans-serif;
    color: var(--caption-grey);
  }
  .design-code--stripe { top: 86px; }
  .design-code--hibiscus { top: 458px; }

  .label {
    position: absolute;
    left: 131px;
    width: 938px;
    height: 274px;
    overflow: hidden;
    box-shadow: 2px 3px 5px rgba(0,0,0,0.3);
  }
  .label--stripe { top: 120px; background: var(--peach); }
  .label--hibiscus { top: 491px; height: 275px; background: var(--white); }

  /* WBL05 */
  .pinstripe-band {
    position: absolute; left: 0; top: 0; width: 100%; height: 109px;
    background: repeating-linear-gradient(90deg, var(--berry) 0 5px, var(--berry-light) 5px 9px);
  }
  .cocoa-band {
    position: absolute; left: 0; top: 109px; width: 100%; height: 21px;
    background: var(--cocoa);
  }
  .berry-rule {
    position: absolute; left: 0; top: 130px; width: 100%; height: 5px;
    background: var(--berry);
  }
  .damask-field {
    position: absolute; left: 0; top: 135px; width: 100%; height: 139px;
    background: linear-gradient(180deg, var(--peach) 0%, var(--peach-pattern) 50%, var(--peach) 100%);
  }
  .stripe-names {
    position: absolute; left: 0; width: 100%; top: 163px;
    text-align: center;
    font: 700 38px/1 "Arimo", Arial, sans-serif;
    color: var(--berry);
  }
  .stripe-date {
    position: absolute; left: 0; width: 100%; top: 209px;
    text-align: center;
    font: 700 24px/1 "Arimo", Arial, sans-serif;
    color: var(--berry);
  }

  /* WBL06 */
  .hibiscus-panel {
    position: absolute; top: 0; height: 100%; width: 297px;
    background: linear-gradient(135deg, var(--lagoon) 0%, var(--lagoon-pattern) 50%, var(--lagoon) 100%);
  }
  .hibiscus-panel--left { left: 0; }
  .hibiscus-panel--right { left: 641px; }
  .panel-edge {
    position: absolute; top: 0; height: 100%; width: 18px;
    background: var(--lagoon-edge);
  }
  .hibiscus-panel--left .panel-edge { right: 0; }
  .hibiscus-panel--right .panel-edge { left: 0; }
  .name-block {
    position: absolute; left: 306px; top: 0; width: 326px; height: 100%;
    background: var(--deep-teal);
    color: var(--white);
    text-align: center;
    font-family: "Cinzel", "Times New Roman", serif;
    font-weight: 700;
  }
  .name-line {
    position: absolute; left: 0; width: 100%;
    font-size: 38px; line-height: 1;
  }
  .name-line--first { top: 58px; }
  .name-line--amp { top: 98px; }
  .name-line--second { top: 134px; }
  .block-date {
    position: absolute; left: 0; width: 100%; top: 197px;
    font-size: 22px; line-height: 1;
  }
</style>
</head>
<body>
  <div class="design-code design-code--stripe">WBL05</div>
  <section class="label label--stripe">
    <div class="pinstripe-band"></div>
    <div class="cocoa-band"></div>
    <div class="berry-rule"></div>
    <div class="damask-field" role="img" aria-label="Faint peach damask ornament pattern"></div>
    <h1 class="stripe-names">HELEN &amp; RAYMOND</h1>
    <p class="stripe-date">May 15, 2011</p>
  </section>

  <div class="design-code design-code--hibiscus">WBL06</div>
  <section class="label label--hibiscus">
    <div class="hibiscus-panel hibiscus-panel--left" role="img" aria-label="Teal hibiscus flower pattern">
      <div class="panel-edge"></div>
    </div>
    <div class="name-block">
      <div class="name-line name-line--first">Helen</div>
      <div class="name-line name-line--amp">&amp;</div>
      <div class="name-line name-line--second">Raymond</div>
      <div class="block-date">May 15, 2011</div>
    </div>
    <div class="hibiscus-panel hibiscus-panel--right" role="img" aria-label="Teal hibiscus flower pattern">
      <div class="panel-edge"></div>
    </div>
  </section>
</body>
</html>
```